Stroomwacht Powerpoint - presentation slides for energy management tool

We need a Powerpoint presentation lay-out which matches our logo from Stroomwacht.nl. 10 slides variations minimum, enough for a full professional presentation to potential clients.
Stroomwacht is a Dutch energymanagement tool for corporate real estate and housing agency. Our clients are Social houseing organisation, real estate owers, property managers and property developers.
Target Market(s)
real estate owners
Property manage
Font styles to use
Sans Serif
Colors
f78f20
0255a3
Requirements
Must have
- Stroomwacht logo colors and style
#F37122 orange
#00345D darkblue
Nice to have
- Professional look, background not white in every slide
Should not have
- wrong color orange and blue.

```html
<!DOCTYPE html>
<html lang="nl">
<head>
<meta charset="utf-8">
<title>Stroomwacht – presentatie-layouts</title>
<link rel="stylesheet" href="https://fonts.googleapis.com/css2?family=Open+Sans:wght@400;700&display=swap">
<style>
  :root {
    --stage: #58585a;
    --paper: #ffffff;
    --orange: #f37122;
    --navy: #07345d;
  }
  html, body {
    margin: 0;
    padding: 0;
    width: 1200px;
    height: 538px;
    overflow: hidden;
    background: var(--stage);
    font-family: "Open Sans", sans-serif;
  }
  .layout-sheet { display: block; width: 1200px; height: 538px; }
  .paper { fill: var(--paper); }
  .orange { fill: var(--orange); }
  .navy { fill: var(--navy); }
  .stripe-navy { stroke: var(--navy); stroke-width: 11; fill: none; }
  .bar-navy { stroke: var(--navy); stroke-width: 17; stroke-linecap: butt; }
  .bar-orange { stroke: var(--orange); stroke-width: 17; stroke-linecap: butt; }
</style>
</head>
<body>
<svg class="layout-sheet" viewBox="0 0 2576 1156" xmlns="http://www.w3.org/2000/svg" aria-label="Tien dia-indelingen in oranje en donkerblauw">
  <defs>
    <clipPath id="clip-slide-diagonal"><rect x="736" y="482" width="418" height="235"/></clipPath>
  </defs>

  <!-- Slide: stepped corner -->
  <g class="slide slide-steps">
    <rect class="paper" x="127" y="75" width="418" height="235"/>
    <rect class="orange" x="127" y="75" width="405" height="26"/>
    <rect class="orange" x="127" y="284" width="280" height="26"/>
    <polygon class="navy" points="530,75 545,75 545,310 407,310 407,250 427,230 441,230 441,199 461,179 476,179 476,147 496,127 511,127 511,95"/>
  </g>

  <!-- Slide: angled frame -->
  <g class="slide slide-angles">
    <rect class="paper" x="736" y="75" width="418" height="235"/>
    <polygon class="navy" points="736,75 1108,75 1105,86 1048,86 958,113 853,86 835,131 736,92"/>
    <polygon class="orange" points="736,92 820,126 812,145 736,117"/>
    <polygon class="orange" points="853,86 958,113 1048,86 1107,86 1106,90 1070,90 960,123 851,95"/>
    <polygon class="orange" points="1110,75 1120,75 1116,88 1144,192 1137,195 1106,86"/>
    <polygon class="navy" points="1120,75 1154,75 1154,310 1138,310 1098,210 1144,192 1116,88"/>
    <polygon class="orange" points="1083,235 1104,226 1138,310 1113,310"/>
  </g>

  <!-- Slide: block grid -->
  <g class="slide slide-blocks">
    <rect class="paper" x="1376" y="75" width="418" height="235"/>
    <rect class="orange" x="1376" y="75" width="418" height="26"/>
    <rect class="navy" x="1376" y="103" width="177" height="90"/>
    <rect class="navy" x="1376" y="196" width="241" height="87"/>
    <rect class="orange" x="1553" y="103" width="241" height="52"/>
    <rect class="orange" x="1617" y="103" width="177" height="86"/>
    <rect class="orange" x="1617" y="191" width="177" height="92"/>
    <rect class="paper" x="1553" y="155" width="64" height="75"/>
    <rect class="navy" x="1376" y="285" width="418" height="25"/>
  </g>

  <!-- Slide: double bands -->
  <g class="slide slide-bands">
    <rect class="paper" x="1994" y="75" width="418" height="235"/>
    <rect class="orange" x="1994" y="75" width="418" height="26"/>
    <rect class="navy" x="1994" y="101" width="334" height="13"/>
    <rect class="navy" x="2078" y="271" width="334" height="13"/>
    <rect class="orange" x="1994" y="284" width="418" height="26"/>
  </g>

  <!-- Slide: crossing lines -->
  <g class="slide slide-cross">
    <rect class="paper" x="127" y="482" width="418" height="235"/>
    <rect class="navy" x="153" y="482" width="26" height="235"/>
    <rect class="navy" x="127" y="503" width="394" height="26"/>
    <rect class="orange" x="494" y="561" width="26" height="156"/>
    <rect class="orange" x="254" y="671" width="291" height="26"/>
  </g>

  <!-- Slide: diagonal hatching -->
  <g class="slide slide-hatch">
    <rect class="paper" x="736" y="482" width="418" height="235"/>
    <rect class="orange" x="842" y="482" width="312" height="26"/>
    <rect class="orange" x="736" y="691" width="314" height="26"/>
    <g clip-path="url(#clip-slide-diagonal)">
      <line class="stripe-navy" x1="846" y1="478" x2="732" y2="592"/>
      <line class="stripe-navy" x1="821" y1="478" x2="732" y2="567"/>
      <line class="stripe-navy" x1="796" y1="478" x2="732" y2="542"/>
      <line class="stripe-navy" x1="771" y1="478" x2="732" y2="517"/>
      <line class="stripe-navy" x1="1158" y1="607" x2="1048" y2="717"/>
      <line class="stripe-navy" x1="1158" y1="632" x2="1073" y2="717"/>
      <line class="stripe-navy" x1="1158" y1="657" x2="1098" y2="717"/>
      <line class="stripe-navy" x1="1158" y1="682" x2="1123" y2="717"/>
      <line class="stripe-navy" x1="1158" y1="707" x2="1148" y2="717"/>
    </g>
  </g>

  <!-- Slide: chevron split -->
  <g class="slide slide-chevron">
    <rect class="paper" x="1376" y="482" width="418" height="235"/>
    <rect class="orange" x="1376" y="482" width="11" height="235"/>
    <polygon class="orange" points="1397,482 1610,482 1518,576 1625,651 1565,717 1397,717"/>
    <polygon class="navy" points="1622,482 1771,482 1771,717 1578,717 1637,651 1530,576"/>
    <rect class="navy" x="1781" y="482" width="13" height="235"/>
  </g>

  <!-- Slide: floating bars -->
  <g class="slide slide-bars">
    <rect class="paper" x="1994" y="482" width="418" height="235"/>
    <rect class="orange" x="1994" y="482" width="115" height="8"/>
    <rect class="navy" x="2297" y="708" width="115" height="9"/>
    <line class="bar-navy" x1="2000" y1="594" x2="2043" y2="637"/>
    <line class="bar-navy" x1="2058" y1="617" x2="2101" y2="660"/>
    <line class="bar-navy" x1="2000" y1="640" x2="2043" y2="683"/>
    <line class="bar-navy" x1="2058" y1="663" x2="2101" y2="706"/>
    <line class="bar-orange" x1="2305" y1="489" x2="2348" y2="532"/>
    <line class="bar-orange" x1="2363" y1="512" x2="2406" y2="555"/>
    <line class="bar-orange" x1="2305" y1="534" x2="2348" y2="577"/>
    <line class="bar-orange" x1="2363" y1="557" x2="2406" y2="600"/>
  </g>

  <!-- Slide: square border -->
  <g class="slide slide-squares">
    <rect class="paper" x="127" y="831" width="418" height="236"/>
    <rect class="navy" x="129" y="831" width="4" height="236"/>
    <rect class="navy" x="133" y="1060" width="412" height="4"/>
    <rect class="orange" x="138" y="831" width="26" height="17"/>
    <rect class="orange" x="138" y="857" width="26" height="25"/>
    <rect class="orange" x="138" y="892" width="26" height="25"/>
    <rect class="orange" x="138" y="926" width="26" height="25"/>
    <rect class="orange" x="138" y="961" width="26" height="25"/>
    <rect class="orange" x="138" y="995" width="26" height="25"/>
    <rect class="orange" x="138" y="1030" width="26" height="25"/>
    <rect class="orange" x="173" y="1030" width="25" height="25"/>
    <rect class="orange" x="207" y="1030" width="26" height="25"/>
    <rect class="orange" x="242" y="1030" width="25" height="25"/>
    <rect class="orange" x="276" y="1030" width="26" height="25"/>
    <rect class="orange" x="311" y="1030" width="25" height="25"/>
    <rect class="orange" x="345" y="1030" width="26" height="25"/>
    <rect class="orange" x="380" y="1030" width="25" height="25"/>
    <rect class="orange" x="414" y="1030" width="26" height="25"/>
    <rect class="orange" x="449" y="1030" width="25" height="25"/>
    <rect class="orange" x="483" y="1030" width="26" height="25"/>
    <rect class="orange" x="518" y="1030" width="27" height="25"/>
  </g>

  <!-- Slide: curved edge -->
  <g class="slide slide-curve">
    <rect class="paper" x="736" y="831" width="418" height="236"/>
    <rect class="navy" x="736" y="831" width="312" height="26"/>
    <path class="orange" d="M1032 831 H1154 V1041 H1083 Q1053 1003 1084 963 L1059 950 L1071 906 Z"/>
    <rect class="navy" x="736" y="1041" width="418" height="26"/>
  </g>
</svg>
</body>
</html>
```